Price Calculator as Responsive Web App to support Sales People

We need to build a simple micro web app to support sales people in making quotes. We already have a backend that can take a number of parameters and create a quote. We need put a responsive web app on top of this so that our people on the road can easily do their price simulations.

We need two pages. One for the input and another for the results. No menus, navigations, etc. It is 6 different inputs as shown with boxes in the sketch. They don't need to be boxed, but some of them have a bit of instruction text that clearly need to belong to the input.

This needs to be responsive, but first and foremost designed for smartphones. I have included a background gradient that we would like to use -- or a variant of it. We expect this to be delivered as HTML/CSS + images so that we can quickly write a few pieces of JavaScript ourselves to wire it up to our price simulator.

Industry/Entity Type

Information Technology

Coding

Coded - Design and coding required

Number of Pages Required

2 page

Font styles to use
Sans Serif

Requirements
Must have
• Responsive design
• Easy to wire up JavaScript to the HTML/CSS
Nice to have
• Some quick way to pick number of months. +/- buttons to add remove a year or 3 months. Same thing with number of items. Add 10 or 5 quickly.
• Maybe some parallax effect while scrolling as long as it is not distracting.
Should not have
• Toolbars, Menus, Navigations, Banners, etc. This is just a single micro app.

```html
<!DOCTYPE html>
<html lang="en">
<head>
<meta charset="utf-8">
<title>Price Calculator</title>
<link href="https://fonts.googleapis.com/css2?family=Montserrat:wght@400;500;600;700&display=swap" rel="stylesheet">
<style>
  :root {
    --navy-deep: #062640;
    --navy: #0b3d63;
    --navy-light: #125585;
    --page-bg: #ececec;
    --card-bg: #ffffff;
    --text: #1c2733;
    --divider: #d9dde1;
    --badge: #1f7be0;
    --step-idle: #eeeeee;
    --step-idle-text: #5b636b;
  }
  * { box-sizing: border-box; margin: 0; padding: 0; }
  html, body { width: 1200px; height: 1120px; overflow: hidden; }
  body {
    position: relative;
    background: var(--page-bg);
    font-family: "Montserrat", sans-serif;
    color: var(--text);
  }

  /* Top bar */
  .app-header {
    position: absolute; left: 0; top: 0; width: 1200px; height: 53px;
    background: linear-gradient(180deg, var(--navy-deep) 0%, var(--navy) 100%);
    border-bottom: 2px solid #6f8799;
  }
  .app-title {
    position: absolute; left: 143px; top: 17px;
    color: #fff; font-size: 14px; font-weight: 500; letter-spacing: 0.3px;
  }
  .header-icon { position: absolute; top: 17px; }
  .header-icon.mail { left: 838px; }
  .header-icon.bell { left: 874px; top: 16px; }
  .badge {
    position: absolute; top: -4px; right: -7px;
    width: 11px; height: 11px; border-radius: 50%;
    background: var(--badge); color: #fff;
    font-size: 7px; font-weight: 700; line-height: 11px; text-align: center;
  }
  .user-menu { position: absolute; left: 933px; top: 11px; display: flex; align-items: center; }
  .avatar {
    width: 31px; height: 31px; border-radius: 50%;
    background: linear-gradient(160deg, #e9d3c4, #b88a72);
    border: 2px solid #fff;
  }
  .user-name { margin-left: 9px; color: #fff; font-size: 12px; font-weight: 500; }
  .user-menu svg { margin-left: 12px; }

  /* Cards */
  .calculator-card {
    position: absolute; left: 144px; top: 77px; width: 678px; height: 952px;
    background: var(--card-bg); padding: 17px 32px 0 30px;
  }
  .steps-card {
    position: absolute; left: 847px; top: 77px; width: 209px; height: 360px;
    background: var(--card-bg); padding: 23px 17px 0 20px;
  }

  .field { padding: 13px 0 12px; border-bottom: 1px solid var(--divider); }
  .field.stepper-field { padding-bottom: 16px; }
  .field-label { font-size: 14px; font-weight: 500; line-height: 18px; }

  /* Stepper */
  .stepper {
    display: flex; margin-top: 11px; margin-left: 2px;
    width: 286px; height: 33px; border-radius: 17px; overflow: hidden;
    background: linear-gradient(180deg, var(--navy-light) 0%, var(--navy-deep) 100%);
  }
  .stepper-btn {
    width: 46px; color: #fff; font-size: 13px; font-weight: 700;
    display: flex; align-items: center; justify-content: center;
    border-right: 1px solid rgba(0,0,0,0.35);
  }
  .stepper-btn:first-child { padding-left: 6px; }
  .stepper-btn:last-child { border-right: none; padding-right: 6px; }
  .stepper-value {
    width: 102px; background: #fff; border: 2px solid var(--navy);
    color: var(--navy-deep); font-size: 13px; font-weight: 700;
    display: flex; align-items: center; justify-content: center;
  }

  /* Radios */
  .radio-list { margin-top: 7px; margin-left: 2px; }
  .radio-option { position: relative; height: 32px; display: flex; align-items: center; font-size: 13px; font-weight: 500; }
  .radio-mark {
    width: 22px; height: 22px; border-radius: 50%;
    border: 2px solid var(--navy); margin-right: 8px; flex: none;
    display: flex; align-items: center; justify-content: center;
  }
  .radio-option.is-checked .radio-mark::after {
    content: ""; width: 12px; height: 12px; border-radius: 50%; background: var(--navy);
  }
  .hint {
    position: absolute; left: 208px; top: 0; height: 32px; width: 182px;
    border-radius: 16px; background: var(--navy);
    color: #fff; font-size: 10px; line-height: 32px; padding-left: 19px;
  }
  .hint::before {
    content: ""; position: absolute; left: -5px; top: 12px;
    border-top: 4px solid transparent; border-bottom: 4px solid transparent;
    border-right: 6px solid var(--navy);
  }

  /* Next */
  .next-btn {
    margin-top: 25px; margin-left: 2px;
    width: 138px; height: 38px; border-radius: 19px;
    background: linear-gradient(180deg, var(--navy-light) 0%, var(--navy-deep) 100%);
    display: flex; align-items: center; color: #fff;
    font-size: 10px; font-weight: 700; letter-spacing: 2.6px;
  }
  .next-btn span { width: 95px; padding-left: 28px; border-right: 1px solid rgba(255,255,255,0.5); line-height: 22px; }
  .next-btn svg { margin-left: 17px; }

  /* Steps */
  .step {
    height: 37px; display: flex; align-items: center; padding-left: 21px;
    clip-path: polygon(10px 0, 100% 0, 100% 100%, 10px 100%, 0 50%);
    font-size: 8px; font-weight: 700; letter-spacing: 2.2px;
  }
  .step + .step { margin-top: 7px; }
  .step-number {
    width: 12px; height: 12px; border-radius: 50%; margin-right: 10px;
    font-size: 7px; letter-spacing: 0; text-align: center; line-height: 12px;
  }
  .step.is-active { background: linear-gradient(180deg, var(--navy-deep), var(--navy)); color: #fff; }
  .step.is-active .step-number { background: #fff; color: var(--navy-deep); }
  .step.is-idle { background: var(--step-idle); color: var(--step-idle-text); }
  .step.is-idle .step-number { background: #fff; color: var(--step-idle-text); }
</style>
</head>
<body>
  <header class="app-header">
    <div class="app-title">PRICE CALCULATOR</div>
    <div class="header-icon mail">
      <svg width="17" height="13" viewBox="0 0 17 13"><rect x="0" y="0" width="17" height="13" rx="1.5" fill="#fff"/><path d="M1 1.5 L8.5 7.5 L16 1.5" fill="none" stroke="#0b3d63" stroke-width="1.4"/></svg>
      <span class="badge">1</span>
    </div>
    <div class="header-icon bell">
      <svg width="15" height="16" viewBox="0 0 15 16"><path d="M7.5 1 C4.5 1 3 3.3 3 6 V10 L1 12.5 H14 L12 10 V6 C12 3.3 10.5 1 7.5 1 Z" fill="#fff"/><circle cx="7.5" cy="14.3" r="1.7" fill="#fff"/></svg>
      <span class="badge">4</span>
    </div>
    <div class="user-menu">
      <div class="avatar" role="img" aria-label="User profile photo"></div>
      <span class="user-name">Hello Harper</span>
      <svg width="10" height="7" viewBox="0 0 10 7"><path d="M1 1.5 L5 5.5 L9 1.5" fill="none" stroke="#fff" stroke-width="2"/></svg>
    </div>
  </header>

  <main class="calculator-card">
    <section class="field stepper-field">
      <div class="field-label">Duration</div>
      <div class="stepper">
        <div class="stepper-btn">-1</div><div class="stepper-btn">-12</div>
        <div class="stepper-value">24 months</div>
        <div class="stepper-btn">+12</div><div class="stepper-btn">+1</div>
      </div>
    </section>

    <section class="field stepper-field">
      <div class="field-label">Count</div>
      <div class="stepper">
        <div class="stepper-btn">-1</div><div class="stepper-btn">-10</div>
        <div class="stepper-value">100 items</div>
        <div class="stepper-btn">+10</div><div class="stepper-btn">+1</div>
      </div>
    </section>

    <section class="field">
      <div class="field-label">Engine Power (beyond standard)</div>
      <div class="radio-list">
        <div class="radio-option is-checked"><span class="radio-mark"></span>$360 / year - bronze power<span class="hint">the basic engine, lorem ipsum...</span></div>
        <div class="radio-option"><span class="radio-mark"></span>$600 / year - silver power</div>
        <div class="radio-option"><span class="radio-mark"></span>$1M / year - gold power</div>
        <div class="radio-option"><span class="radio-mark"></span>$3M / year - platinum power</div>
      </div>
    </section>

    <section class="field">
      <div class="field-label">Shared storage addition</div>
      <div class="radio-list">
        <div class="radio-option is-checked"><span class="radio-mark"></span>10kg</div>
        <div class="radio-option"><span class="radio-mark"></span>50kg</div>
        <div class="radio-option"><span class="radio-mark"></span>100kg</div>
        <div class="radio-option"><span class="radio-mark"></span>500kg</div>
        <div class="radio-option"><span class="radio-mark"></span>1ton</div>
      </div>
    </section>

    <section class="field">
      <div class="field-label">Additional Tip</div>
      <div class="radio-list">
        <div class="radio-option is-checked"><span class="radio-mark"></span>15%</div>
        <div class="radio-option"><span class="radio-mark"></span>18%</div>
        <div class="radio-option"><span class="radio-mark"></span>20%</div>
      </div>
    </section>

    <section class="field">
      <div class="field-label">Elastic extension</div>
      <div class="radio-list">
        <div class="radio-option is-checked"><span class="radio-mark"></span>30%</div>
        <div class="radio-option"><span class="radio-mark"></span>50%</div>
      </div>
    </section>

    <div class="next-btn">
      <span>NEXT</span>
      <svg width="8" height="14" viewBox="0 0 8 14"><path d="M1 1 L7 7 L1 13" fill="none" stroke="#fff" stroke-width="1.6"/></svg>
    </div>
  </main>

  <aside class="steps-card">
    <div class="step is-active"><span class="step-number">1</span>CALCULATE PRICE</div>
    <div class="step is-idle"><span class="step-number">2</span>RESULT</div>
  </aside>
</body>
</html>
```